UK based media owner TALVEX (http://www.talvex.uk/) needs DIGITAL ADVERT to run on our digital panel

Hi guys,

Thanks for taking the time to have a look at this brief.
I need someone to create a digital advert (still/static design or video) to run on our digital panels which are located across UK university student unions.
For who wants to upload a video ---> All of our panels are digitally enabled and allow for full motion video – they run adverts 10 seconds long (see artwork specification document in attachment) therefore the advert will have to be 10 seconds long.
For static/still design ----> see artwork specification to see resolution etc

I need something professional looking, polished yet fresh and exciting so that it speaks and connects to this younger audience – we want to inspire them to take a step towards new levels of business opportunities.

Here are some Key Points you’ll need to take into consideration when designing the advert:

Overall Campaign Objective: To excite and attract young entrepreneurs to get in touch with us for possible partnerships

Target Audience: Young entrepreneurs attending university (university students – 18 to 24 years old)

Creative Specifications: See attached document with artwork specifications

Text on Advert:

I need the following text to appear on the advert: (Please include company logo)

“Do you have a business idea that would benefit with advertising on these screens?

We want to support young entrepreneurs and will partner with any whom have a great idea

WE WANT TO HEAR FROM YOU!

Email us at ideas@talvex.uk
www.talvex.uk/ideas”

I would need some ideas by the 3rd July 2018 if possible.

Thanks to all who will take part in this project – contact me if you have any questions

Target Market(s)

Young entrepreneurs attending university (university students – 18 to 24 years old)

Requirements
Must have
• I need the following text to appear on the advert: (Please include company logo)
• “Do you have a business idea that would benefit with advertising on these screens?
• We want to support young entrepreneurs and will partner with any whom have a great idea
• WE WANT TO HEAR FROM YOU!
• Email us at ideas@talvex.uk
• www.talvex.uk/ideas”

```html
<!DOCTYPE html>
<html lang="en">
<head>
<meta charset="utf-8">
<title>TALVEX – Young Entrepreneurs Advert</title>
<link rel="stylesheet" href="https://fonts.googleapis.com/css2?family=Oswald:wght@700&family=Open+Sans:wght@400;700&display=swap">
<style>
  :root {
    --brand-red: #f2000f;
    --band-red: #cc1f28;
    --ink: #1a1a1a;
    --panel-dark: #231f20;
    --paper: #ffffff;
  }
  html, body {
    margin: 0;
    padding: 0;
    overflow: hidden;
    background: var(--paper);
  }
  .advert {
    position: relative;
    width: 675px;
    height: 1200px;
    overflow: hidden;
    background: var(--paper);
    font-family: "Open Sans", Arial, sans-serif;
  }
  .top-band {
    position: absolute;
    left: 0; top: 0;
    width: 100%;
    height: 46px;
    background: var(--band-red);
  }
  .brand-name {
    position: absolute;
    left: 0; top: 150px;
    width: 100%;
    text-align: center;
    font-family: "Oswald", "Arial Narrow", sans-serif;
    font-weight: 700;
    font-size: 128px;
    line-height: 1;
    color: var(--brand-red);
    letter-spacing: 2px;
    margin: 0;
  }
  .headline {
    position: absolute;
    left: 0; top: 380px;
    width: 100%;
    margin: 0;
    text-align: center;
    font-family: "Oswald", "Arial Narrow", sans-serif;
    font-weight: 700;
    font-size: 62px;
    line-height: 58px;
    letter-spacing: -1.5px;
    color: var(--brand-red);
  }
  .intro {
    position: absolute;
    left: 0; top: 660px;
    width: 100%;
    margin: 0;
    text-align: center;
    font-size: 29px;
    line-height: 44px;
    color: var(--ink);
  }
  .callout-panel {
    position: absolute;
    left: 0; top: 818px;
    width: 100%;
    height: 202px;
    background: var(--panel-dark);
    display: flex;
    align-items: center;
    justify-content: center;
  }
  .callout {
    margin: 0;
    text-align: center;
    font-family: "Oswald", "Arial Narrow", sans-serif;
    font-weight: 700;
    font-size: 72px;
    line-height: 76px;
    letter-spacing: -2px;
    color: var(--brand-red);
    text-transform: uppercase;
  }
  .email {
    position: absolute;
    left: 0; top: 1038px;
    width: 100%;
    margin: 0;
    text-align: center;
    font-size: 32px;
    line-height: 44px;
    color: var(--brand-red);
  }
  .web-band {
    position: absolute;
    left: 0; top: 1090px;
    width: 100%;
    height: 110px;
    background: var(--brand-red);
    display: flex;
    align-items: center;
    justify-content: center;
  }
  .web-address {
    margin: 0;
    font-weight: 700;
    font-size: 35px;
    color: var(--paper);
  }
</style>
</head>
<body>
  <main class="advert">
    <div class="top-band"></div>

    <p class="brand-name">TALVEX</p>

    <h1 class="headline">Do you have a business<br>idea that would benefit<br>with advertising on<br>these screens?</h1>

    <p class="intro">We want to support young<br>entrepreneurs and will partner with<br>any whom have a great idea</p>

    <section class="callout-panel">
      <h2 class="callout">We want to hear<br>from you!</h2>
    </section>

    <p class="email">Email us at ideas@talvex.uk</p>

    <footer class="web-band">
      <p class="web-address">www.talvex.uk/ideas</p>
    </footer>
  </main>
</body>
</html>
```